Window Cleaning Leaflet

Hi everyone,

I need a leaflet (couldn't find 'leaflet' as an option when begining this project - so one sided only) to send out to coastal properties in South side Melbourne. The Flyer is aimed at high net individuals, mummies, business people etc who own these properties who don't have time to clean the windows themselves (often multiple levels) and want their home looking fabulous in time for Christmas and NY's celebrations.

I would really love a new and original design for a window washing leaflet. something outside of the norm that 'pops' and makes people feel happy when they look at it.

I guess a point of differentiation is that I'm a female working in a mans industry so appeal to mothers looking for someone who is 'reliable, trustworthy and understanding of peoples needs'.

I have made an outline of what I would like included in the leaflet, so if you could please take a look, feel free to change things around, wording and layout etc. If you can make it sound more professional please do so.

I would like the colours to be 'happy' colours, maybe with a silly season theme?

Overall aesthetically pleasing is a must, I find most window cleaning leaflets fairly mundane and boring, please feel free to think outside the box. The more original the better.

Target Market(s)

People who own large Melbourne homes in affluent suburbs, mainly suburbs with a lot of large coastal properties. Generally owned by high net worth individuals who just don't have tme to clean the windows themselves due to their profession or hectic lifestyles but can afford to pay someone else to do it.

Industry/Entity Type

Window Cleaning

Requirements
Must have
• 1) The name of the business - Tilda’s Glass Gleaming Services
• 2) The coupon special and all details attached:
• Small Homes (up to 12 windows) $120
• Medium Homes (up to 16 windows) $180
• Large Homes (up to 20 windows, 2 storeys) $240
• 20% discount
• *Discount applicable to first time customers only.
• *All services include fly screen, sill and tracks cleaned as well as cobweb removal.
• *Houses with more than 20 windows (or two levels) will have an immediate quote provided upon inspection of the property with 20% discount applied.
• *Tilda’s Glass Gleaming Services are fully insured.
• 3) My contact number - 0418 263 591

```html
<!DOCTYPE html>
<html lang="en">
<head>
<meta charset="utf-8">
<title>Tilda’s Glass Gleaming Services – Christmas Leaflet</title>
<link href="https://fonts.googleapis.com/css2?family=Open+Sans:ital,wght@0,400;0,600;0,700;1,600;1,700&display=swap" rel="stylesheet">
<style>
  :root {
    --red: #e8382f;
    --panel-red: #cf4832;
    --panel-salmon: #dc7256;
    --divider: #eaa08a;
    --yellow: #fff21c;
    --ink: #222222;
    --white: #ffffff;
    --room-light: #f4f1ec;
    --room-mid: #e3ddd3;
  }
  * { box-sizing: border-box; margin: 0; padding: 0; }
  html, body { width: 1200px; height: 848px; overflow: hidden; background: var(--white); }
  body { font-family: "Open Sans", Arial, sans-serif; color: var(--ink); }

  .leaflet { position: relative; width: 1200px; height: 848px; overflow: hidden; background: var(--white); }

  .room-backdrop {
    position: absolute; left: 0; top: 0; width: 1200px; height: 640px;
    background: linear-gradient(90deg, #dfe3dc 0%, var(--room-light) 35%, #faf8f4 55%, var(--room-mid) 80%, #e9e2d6 100%);
  }
  .room-fade {
    position: absolute; left: 0; top: 560px; width: 1200px; height: 90px;
    background: linear-gradient(180deg, rgba(255,255,255,0), var(--white));
  }
  .festive-decor {
    position: absolute; left: 0; top: 0; width: 800px; height: 90px;
    background: linear-gradient(180deg, rgba(63,138,58,.55), rgba(63,138,58,0));
  }
  .squeegee { position: absolute; left: 1044px; top: 82px; width: 92px; height: 166px; background: linear-gradient(90deg, #d4d7da, #eceded); }
  .client-photo {
    position: absolute; left: 800px; top: 300px; width: 250px; height: 548px;
    background: linear-gradient(180deg, #cdbdb2 0%, #ececec 40%, #dedcd4 100%);
  }
  .gift-bow {
    position: absolute; left: 970px; top: 580px; width: 230px; height: 268px;
    background: linear-gradient(135deg, #e59a9c, #c8141e);
  }

  .brand-name { position: absolute; left: 66px; top: 92px; font-size: 26px; font-weight: 600; font-style: italic; color: var(--ink); white-space: nowrap; }
  .headline { position: absolute; left: 66px; top: 132px; font-size: 51.5px; font-weight: 700; color: var(--red); letter-spacing: -.3px; white-space: nowrap; }
  .subhead { position: absolute; left: 66px; top: 191px; font-size: 29px; color: var(--ink); white-space: nowrap; }

  .offer-panel { position: absolute; left: 42px; top: 260px; width: 425px; height: 334px; background: var(--panel-red); color: var(--white); padding: 30px 28px; border-radius: 4px 0 0 4px; }
  .offer-panel p { font-size: 18px; line-height: 25px; white-space: nowrap; }
  .offer-panel .highlight { background: var(--white); color: var(--red); font-weight: 700; padding: 0 3px; }
  .offer-panel .spacer { margin-top: 22px; }
  .offer-panel .call { margin-top: 22px; font-size: 20px; line-height: 28px; font-weight: 600; font-style: italic; }
  .offer-panel .phone { margin-top: 16px; font-size: 30px; font-weight: 700; font-style: italic; color: var(--yellow); letter-spacing: .8px; }

  .price-table { position: absolute; left: 467px; top: 260px; width: 300px; height: 334px; background: var(--panel-salmon); border-radius: 0 4px 4px 0; }
  .price-row { position: relative; height: 111px; border-bottom: 2px solid var(--divider); color: var(--white); }
  .price-row:last-child { border-bottom: none; }
  .price-row .size { position: absolute; left: 18px; bottom: 8px; font-size: 17px; line-height: 24px; white-space: nowrap; }
  .price-row .amount { position: absolute; right: 20px; top: 22px; font-size: 40px; font-weight: 700; color: var(--yellow); }
  .home-icon { position: absolute; left: 18px; top: 20px; }

  .discount-badge {
    position: absolute; left: 62px; top: 640px; width: 200px; height: 165px;
    background: linear-gradient(135deg, #f3a3b8, #f2c48a);
  }
  .discount-tile { position: absolute; left: 134px; top: 693px; width: 96px; height: 96px; background: var(--white); border-radius: 16px; box-shadow: 0 4px 10px rgba(0,0,0,.25); text-align: center; color: var(--ink); font-weight: 700; padding-top: 10px; }
  .discount-tile .pct { font-size: 34px; line-height: 38px; }
  .discount-tile .off { font-size: 20px; letter-spacing: 6px; }

  .terms { position: absolute; left: 306px; top: 630px; list-style: none; }
  .terms li { position: relative; padding-left: 32px; font-size: 15px; line-height: 20px; margin-bottom: 10px; white-space: nowrap; }
  .terms li svg { position: absolute; left: 0; top: 0; }
</style>
</head>
<body>
<main class="leaflet">
  <div class="room-backdrop" role="img" aria-label="Bright living room with tall white-framed windows"></div>
  <div class="room-fade"></div>
  <div class="festive-decor" role="img" aria-label="Christmas garland with hanging baubles"></div>
  <div class="squeegee" role="img" aria-label="Window squeegee"></div>
  <div class="client-photo" role="img" aria-label="Woman sipping from a mug by a window"></div>
  <div class="gift-bow" role="img" aria-label="Red gift ribbon and bow"></div>

  <h2 class="brand-name">Tilda’s Glass Gleaming Services</h2>
  <h1 class="headline">Do you need your windows cleaned?</h1>
  <p class="subhead">Are you simply too busy as a hard working parent to do it yourself?</p>

  <section class="offer-panel">
    <p>Tilda understands and wants to help you<br>enjoy your home looking its best <span class="highlight">before</span><br><span class="highlight">Christmas and NY’s celebrations begin</span>!</p>
    <p class="spacer">We provide a reliable, professional service,<br>ensuring that your home will sparkle
      <svg width="16" height="16" viewBox="0 0 16 16" aria-hidden="true"><path d="M8 0l1.6 5 4.4-2.6-2.6 4.4L16 8l-4.6 1.2L14 13.6 9.6 11 8 16l-1.6-5L2 13.6l2.6-4.4L0 8l4.6-1.2L2 2.4 6.4 5z" fill="#fff"/></svg>
    </p>
    <p class="call">Call Tilda today and take advantage<br>of our special introductory offer.</p>
    <p class="phone">Tilda - 0418 263 591</p>
  </section>

  <section class="price-table">
    <div class="price-row">
      <svg class="home-icon" width="32" height="30" viewBox="0 0 32 30" aria-hidden="true"><path d="M16 0L0 15h5v15h8v-9h6v9h8V15h5z" fill="#fff21c"/></svg>
      <span class="size">Small Homes<br>(up to 12 windows)</span>
      <span class="amount">$120</span>
    </div>
    <div class="price-row">
      <span class="size">Medium Homes<br>(up to 16 windows)</span>
      <span class="amount">$180</span>
    </div>
    <div class="price-row">
      <span class="size">Large Homes<br>(up to 20 windows, 2 storeys)</span>
      <span class="amount">$240</span>
    </div>
  </section>

  <div class="discount-badge" role="img" aria-label="Colourful splash behind discount tile"></div>
  <div class="discount-tile"><div class="pct">20%</div><div class="off">OFF</div></div>

  <ul class="terms">
    <li><svg width="20" height="20" viewBox="0 0 20 20" aria-hidden="true"><path d="M10 2c3 0 5 2.5 5 6v4l2 3H3l2-3V8c0-3.5 2-6 5-6z" fill="#e8382f"/><circle cx="10" cy="17" r="2" fill="#e8382f"/></svg>Discount applicable to first time customers only.</li>
    <li><svg width="20" height="20" viewBox="0 0 20 20" aria-hidden="true"><path d="M10 2c3 0 5 2.5 5 6v4l2 3H3l2-3V8c0-3.5 2-6 5-6z" fill="#f4a62a"/><circle cx="10" cy="17" r="2" fill="#f4a62a"/></svg>All services include fly screen, sill and tracks cleaned<br>as well as cobweb removal.</li>
    <li><svg width="20" height="20" viewBox="0 0 20 20" aria-hidden="true"><path d="M10 2c3 0 5 2.5 5 6v4l2 3H3l2-3V8c0-3.5 2-6 5-6z" fill="#e8382f"/><circle cx="10" cy="17" r="2" fill="#e8382f"/></svg>Houses with more than 20 windows (or two levels) will<br>have an immediate quote provided upon inspection of<br>the property with 20% discount applied.</li>
    <li><svg width="20" height="20" viewBox="0 0 20 20" aria-hidden="true"><path d="M10 2c3 0 5 2.5 5 6v4l2 3H3l2-3V8c0-3.5 2-6 5-6z" fill="#f4a62a"/><circle cx="10" cy="17" r="2" fill="#f4a62a"/></svg>Tilda’s Glass Gleaming Services are fully insured.</li>
  </ul>
</main>
</body>
</html>
```